Business Card Design Project

I want a cleaner business card and envelope then what we have now, its too crowded.
Updates

I update with logo, this can be changed anyway you feel it looks best. I also have put gaurantee on there and extended time, this is my first time doing this. Also gave an example of current card

Target Market(s)

a wide array of customers from lattice 700 to small companies and cleints

Industry/Entity Type

Business

Requirements
Must have
• Need to have address, telephone number email
Nice to have
• a sharp professional card that stands out but is still very clean.
Should not have
• Not crazy looking

```html
<!DOCTYPE html>
<html lang="en">
<head>
<meta charset="utf-8">
<title>Brisley Group Business Card</title>
<link href="https://fonts.googleapis.com/css2?family=Arimo:wght@400;700&display=swap" rel="stylesheet">
<style>
  :root {
    --stage: #0d2c36;
    --paper: #ffffff;
    --brand-blue: #1a5f97;
    --deep-blue: #15589a;
    --sky-blue: #4aa7dd;
    --pale-blue: #8fc9ea;
    --ink: #111111;
    --rule: #333333;
  }
  * { box-sizing: border-box; margin: 0; padding: 0; }
  html, body {
    width: 1200px; height: 798px; overflow: hidden;
    background: var(--stage);
    font-family: "Arimo", Arial, sans-serif;
  }
  .canvas { position: relative; width: 1200px; height: 798px; }
  .card {
    position: absolute; width: 560px; height: 320px; overflow: hidden;
    box-shadow: 0 12px 30px rgba(0,0,0,.45);
  }
  .card-front { left: 60px; top: 60px; background: var(--paper); }
  .card-back {
    left: 580px; top: 418px;
    background: linear-gradient(135deg, #2a86c8 0%, var(--deep-blue) 100%);
  }

  .decor-panel { position: absolute; left: 0; top: 0; bottom: 0; }
  .card-front .decor-panel {
    width: 210px;
    background: linear-gradient(160deg, var(--sky-blue) 0%, var(--brand-blue) 100%);
  }
  .card-back .decor-panel {
    width: 190px;
    background: linear-gradient(160deg, var(--pale-blue) 0%, var(--sky-blue) 100%);
  }

  .brand { position: absolute; display: flex; align-items: center; gap: 8px; font-weight: 700; font-size: 17px; letter-spacing: .5px; }
  .brand-mark { width: 12px; height: 12px; background: currentColor; }
  .card-front .brand { left: 370px; top: 58px; color: var(--brand-blue); }
  .card-back .brand { left: 345px; top: 62px; color: var(--paper); }

  .person { position: absolute; left: 258px; top: 158px; color: var(--ink); }
  .person-name { font-size: 23px; font-weight: 400; letter-spacing: .5px; }
  .person-role { font-size: 12px; margin-left: 6px; }
  .person-mobile { font-size: 14px; margin-top: 2px; letter-spacing: .3px; }

  .company { position: absolute; left: 258px; top: 218px; right: 0; }
  .company-name { font-size: 13.5px; font-weight: 700; color: var(--ink); padding-bottom: 4px; border-bottom: 1.5px solid var(--rule); }
  .contact-list { list-style: none; margin-top: 5px; font-size: 9.5px; font-weight: 700; color: var(--ink); line-height: 14px; }
  .contact-list li::before { content: ""; display: inline-block; width: 6px; height: 6px; background: var(--ink); margin-right: 8px; vertical-align: 1px; }

  .tagline { position: absolute; right: 56px; bottom: 44px; color: var(--paper); font-weight: 700; font-size: 19px; letter-spacing: .5px; display: flex; align-items: center; gap: 6px; }
  .tagline-mark { width: 13px; height: 13px; background: var(--paper); }
</style>
</head>
<body>
<main class="canvas">

  <section class="card card-front" aria-label="Business card front">
    <div class="decor-panel" role="img" aria-label="Curved blue swoosh decoration with a light and orange accent stripe"></div>
    <div class="brand"><span class="brand-mark"></span>BRISLEY GROUP</div>
    <div class="person">
      <div><span class="person-name">NAME</span><span class="person-role">Manager</span></div>
      <div class="person-mobile">M:135550101234</div>
    </div>
    <div class="company">
      <div class="company-name">NORTH BRISLEY GROUP CO., LTD</div>
      <ul class="contact-list">
        <li>ADD:&nbsp; Fenwick eastgate district, 42</li>
        <li>TEL:&nbsp; 0555-0142888&nbsp;&nbsp;&nbsp; 0142999</li>
        <li>E-MAIL:cs0142office@example.com</li>
      </ul>
    </div>
  </section>

  <section class="card card-back" aria-label="Business card back">
    <div class="decor-panel" role="img" aria-label="Curved light blue swoosh decoration with accent stripes and a trail of dots"></div>
    <div class="brand"><span class="brand-mark"></span>BRISLEY GROUP</div>
    <div class="tagline">KESTREL<span class="tagline-mark"></span></div>
  </section>

</main>
</body>
</html>
```